eBook Cover for Fantasy Novel called "The Quiet Meadow"

Fantasy novel eBook Cover based on the samples provided. I'm looking for something simple and reminiscent of the classic fairy tale covers. I would like a blue (similar to "Wandering Lanterns" cover) for the background. The "bear with antlers" is supposed to be the symbol for a medieval kingdom. I'm not an artist so I did the best I could with my sketch - I am looking for something like this, but cleaner with more detailed antlers. I used a silhouette of a bear and one of an elk to make this sketch - like classic medieval crests/sigils. I would like the bear to be a solid silhouette that is a soft gold color. Please disregard the circular pattern in the background of my sketch. I want the bear, the title (The Quiet Meadow), the name (Mira Holloway), and a border of simple roses on a blue background. I don't want anything too fancy for the roses/leaves, maybe something similar to the sketch of the rose I included. More contemporary and less "Grandma's couch/sweater". As for the font, I would prefer, if not like the script in my sketch (albeit cleaned up and nicer) then something close to it. I am wanting something close to handwriting but not too formal or childish. I included several examples of a super poor quality cover that I threw together just for reference as to orientation and size of things. Depending on how big the roses and the bear are will help determine the best placement for the text. I am wanting something eye catching and intriguing to help attract readers. The sample book cover ("Wandering Lanterns") has colors/tones that I really like, however I don't want something this busy.

EDIT: The bear is supposed to be a coat of arms. Like the medieval crests/sigils I have added to this brief. Similar to the one I sketched. As if it were sewn into banners or tapestries or painted on shields, that kind of thing.

Target Market(s)

Adults ages 20-ish and up. Although it is a fantasy novel, it has adult themes and elements to it.

Industry/Entity Type

Writing

Requirements
Must have
• The publishing guidelines for cover images : JPEG or TIFF files, the ideal image dimensions is 2,560 x 1,600 pixels, less than 50MB, avoid compressing, minimum resolution 300 PPI, and color should be RGB.
Nice to have
• Please refer to the project description.
Should not have

```html
<!DOCTYPE html>
<html lang="en">
<head>
<meta charset="utf-8">
<title>The Quiet Meadow — Cover</title>
<link href="https://fonts.googleapis.com/css2?family=Great+Vibes&family=Cinzel:wght@400;600&display=swap" rel="stylesheet">
<style>
  :root {
    --page-bg: #ffffff;
    --cover-blue: #1d3f8f;
    --cover-blue-deep: #142d6b;
    --panel-top: #35597f;
    --panel-mid: #1e3d6e;
    --panel-bottom: #173467;
    --forest: #1a3560;
    --shield-light: #b9bcbf;
    --shield-dark: #6f7378;
    --shield-rim: #1b1b1d;
    --gold-light: #f6dc8c;
    --gold: #d6a640;
    --gold-dark: #8c6320;
    --author-ink: #f4efe2;
  }
  * { margin: 0; padding: 0; box-sizing: border-box; }
  html, body {
    width: 1200px;
    height: 1073px;
    overflow: hidden;
    background: var(--page-bg);
  }
  .canvas {
    position: relative;
    width: 1200px;
    height: 1073px;
    background: var(--page-bg);
  }
  .cover {
    position: absolute;
    left: 247px;
    top: 40px;
    width: 653px;
    height: 987px;
    background: radial-gradient(ellipse at 50% 45%, var(--cover-blue) 0%, var(--cover-blue-deep) 100%);
  }
  .cover-panel {
    position: absolute;
    left: 63px;
    top: 62px;
    width: 527px;
    height: 865px;
    background:
      radial-gradient(ellipse at 50% 60%, rgba(60, 95, 150, 0.35) 0%, rgba(0, 0, 0, 0) 60%),
      linear-gradient(180deg, var(--panel-top) 0%, var(--panel-mid) 28%, var(--forest) 45%, var(--panel-bottom) 100%);
    box-shadow: inset 0 0 24px rgba(5, 15, 45, 0.55);
  }
  .crest {
    position: absolute;
    left: 259px;
    top: 145px;
    width: 136px;
    height: 186px;
  }
  .title {
    position: absolute;
    left: 63px;
    top: 420px;
    width: 527px;
    text-align: center;
    font-family: "Great Vibes", cursive;
    font-weight: 400;
    line-height: 1.12;
    background: linear-gradient(180deg, var(--gold-light) 0%, var(--gold) 55%, var(--gold-dark) 100%);
    -webkit-background-clip: text;
    background-clip: text;
    color: transparent;
    filter: drop-shadow(0 3px 4px rgba(5, 12, 35, 0.7));
  }
  .title-line { display: block; }
  .title-line--first { font-size: 112px; padding-right: 10px; }
  .title-line--second { font-size: 138px; padding-left: 30px; }
  .author {
    position: absolute;
    left: 0;
    top: 880px;
    width: 653px;
    text-align: center;
    font-family: "Cinzel", serif;
    font-weight: 600;
    font-size: 25px;
    letter-spacing: 1px;
    color: var(--author-ink);
  }
</style>
</head>
<body>
  <div class="canvas">
    <div class="cover">
      <div class="cover-panel" role="img" aria-label="Misty night sky over a dark blue forest"></div>

      <svg class="crest" viewBox="0 0 136 186" role="img" aria-label="Heraldic shield emblem of the kingdom">
        <defs>
          <linearGradient id="shieldFace" x1="0" y1="0" x2="1" y2="1">
            <stop offset="0" stop-color="var(--shield-light)"/>
            <stop offset="1" stop-color="var(--shield-dark)"/>
          </linearGradient>
        </defs>
        <path d="M4 14 Q68 -2 132 14 L132 92 Q128 150 68 184 Q8 150 4 92 Z" fill="var(--shield-rim)"/>
        <path d="M12 20 Q68 6 124 20 L124 92 Q120 143 68 174 Q16 143 12 92 Z" fill="url(#shieldFace)"/>
      </svg>

      <h1 class="title">
        <span class="title-line title-line--first">The Quiet</span>
        <span class="title-line title-line--second">Meadow</span>
      </h1>

      <p class="author">Mira Holloway</p>
    </div>
  </div>
</body>
</html>
```